Talbek vodka

With the logo attached in the subsequent file, a business card that reflects a premium and organic vodka. On the first side, the company logo in large. The names must be included on the back of the card (Mateo Ignacio Dalmau Ferrerons with the number +34 655 219 870 and Oriol Batlle Quintana and +34 677 341 592). The slogan "What binds us" and "Organic and permium vodka" in bold E-mail (talbekvodka@mailora.net); Website www.talbekvodkaorg.net

```html
<!DOCTYPE html>
<html lang="en">
<head>
<meta charset="utf-8">
<title>Talbek vodka – business card</title>
<link href="https://fonts.googleapis.com/css2?family=Open+Sans:wght@400;600;700&display=swap" rel="stylesheet">
<style>
  :root {
    --backdrop: #e4e2df;
    --card-white: #ffffff;
    --card-grey: #808080;
    --ink: #858585;
    --ink-soft: #8e8e8e;
    --rule: #9a9a9a;
    --stripe-dark: #7a7a7c;
    --stripe-light: #b0b0b0;
    --on-grey: #ffffff;
  }
  * { box-sizing: border-box; margin: 0; padding: 0; }
  html, body { width: 1200px; height: 1040px; overflow: hidden; }
  body {
    background: var(--backdrop);
    font-family: "Open Sans", Arial, sans-serif;
    position: relative;
  }
  .card {
    position: absolute;
    left: 285px;
    width: 640px;
    height: 366px;
    box-shadow: 0 2px 6px rgba(0,0,0,0.25);
    overflow: hidden;
  }
  .card--front { top: 130px; background: var(--card-white); }
  .card--back { top: 567px; background: var(--card-grey); }

  .brand-name {
    position: absolute;
    left: 387px;
    top: 100px;
    width: 214px;
    text-align: center;
    font-size: 38px;
    font-weight: 600;
    color: var(--ink-soft);
    letter-spacing: 0.5px;
    white-space: nowrap;
  }

  .person { position: absolute; top: 237px; color: var(--ink); }
  .person--first { left: 39px; }
  .person--second { left: 287px; }
  .person__name { font-size: 20px; font-weight: 600; line-height: 26px; white-space: nowrap; }
  .person__phone { font-size: 16px; font-weight: 400; line-height: 22px; white-space: nowrap; }

  .divider-vertical {
    position: absolute; left: 272px; top: 246px;
    width: 1px; height: 34px; background: var(--rule);
  }
  .divider-horizontal {
    position: absolute; left: 38px; top: 294px;
    width: 552px; height: 1px; background: var(--rule);
  }

  .contact {
    position: absolute; left: 38px; top: 302px;
    display: flex; align-items: center; gap: 8px;
    font-size: 15px; color: var(--ink); white-space: nowrap;
  }
  .contact__icon { width: 15px; height: 15px; flex: none; }
  .contact__gap { width: 4px; }

  .stripe { position: absolute; left: 0; bottom: 0; width: 640px; height: 11px; }

  .back-mark {
    position: absolute; left: 147px; top: 82px;
    width: 348px; height: 188px;
    display: flex; align-items: center; justify-content: center;
    font-size: 40px; font-weight: 600; color: var(--on-grey);
    white-space: nowrap;
  }
  .slogan {
    position: absolute; left: 0; top: 290px; width: 640px;
    text-align: center; color: var(--on-grey);
    font-size: 16px; font-weight: 700; line-height: 21px;
    text-transform: uppercase;
  }
</style>
</head>
<body>

<section class="card card--front" aria-label="Card front">
  <div class="brand-name">Talbek vodka</div>

  <div class="person person--first">
    <p class="person__name">Oriol Batlle Quintana</p>
    <p class="person__phone">+34 677 341 592</p>
  </div>
  <div class="divider-vertical"></div>
  <div class="person person--second">
    <p class="person__name">Mateo Ignacio Dalmau Ferrerons</p>
    <p class="person__phone">+34 655 219 870</p>
  </div>

  <div class="divider-horizontal"></div>

  <div class="contact">
    <svg class="contact__icon" viewBox="0 0 16 16" aria-hidden="true">
      <rect x="1" y="4" width="14" height="9" fill="#8a8a8a"/>
      <path d="M1 4 L8 9 L15 4" fill="none" stroke="#fff" stroke-width="1.2"/>
    </svg>
    <span>talbekvodka@mailora.net</span>
    <span class="contact__gap"></span>
    <svg class="contact__icon" viewBox="0 0 16 16" aria-hidden="true">
      <circle cx="8" cy="8" r="7" fill="#8a8a8a"/>
      <path d="M1 8 H15 M8 1 C4 5 4 11 8 15 M8 1 C12 5 12 11 8 15" fill="none" stroke="#fff" stroke-width="1"/>
    </svg>
    <span>www.talbekvodkaorg.net</span>
  </div>

  <svg class="stripe" viewBox="0 0 640 11" preserveAspectRatio="none" aria-hidden="true">
    <polygon points="0,0 418,0 414,11 0,11" fill="var(--stripe-dark)"/>
    <polygon points="423,0 640,0 640,11 419,11" fill="var(--stripe-light)"/>
  </svg>
</section>

<section class="card card--back" aria-label="Card back">
  <div class="back-mark">Talbek vodka</div>
  <div class="slogan">
    <p>What binds us</p>
    <p>Organic &amp; Permium vodka</p>
  </div>
</section>

</body>
</html>
```